Security Services Business Card

Looking for a clean modern style business card design for a residential and commercial security solutions provider. We install and service the following
security alarm, access control, video surveillance and fire alarm. Attached are the front and back of our current business cards in PSD file format.

Target Market(s)

Security alarm clients in the commercial and residential markets

Industry/Entity Type

Security Service

Contact Information for Business Card

We are open to designers suggestion and or design ideas.

Font styles to use
Serif
Sans Serif

Colors
3276b5
33a6d7
fffefd

Requirements
Must have
• Must have company logo , first and last name , phone number , web and email address, ect....

```html
<!DOCTYPE html>
<html lang="en">
<head>
<meta charset="utf-8">
<title>Brightwall Systems – Business Card</title>
<link rel="stylesheet" href="https://fonts.googleapis.com/css2?family=Open+Sans:wght@700;800&family=Roboto:wght@300;400&display=swap">
<style>
  :root {
    --brand-blue: #3276b5;
    --brand-deep: #2a62a6;
    --brand-sky: #33a6d7;
    --paper: #fffefd;
    --backdrop: #d8d8d6;
  }
  html, body {
    margin: 0;
    width: 1200px;
    height: 1200px;
    overflow: hidden;
    background: var(--backdrop);
  }
  .card-slot {
    position: absolute;
    left: 262px;
    width: 686px;
    height: 392px;
    box-shadow: 0 14px 24px rgba(0,0,0,0.22);
  }
  .card-slot--front { top: 165px; }
  .card-slot--back  { top: 653px; }
  .card {
    position: absolute;
    top: 0; left: 0;
    width: 800px;
    height: 457px;
    transform: scale(0.8575);
    transform-origin: 0 0;
    overflow: hidden;
  }
  .card--front { background: var(--paper); }
  .card--back {
    background: linear-gradient(200deg, #4f8cc6 0%, var(--brand-blue) 45%, #255ea3 100%);
    color: var(--paper);
  }
  .card__shapes {
    position: absolute;
    inset: 0;
  }
  .brand-name {
    position: absolute;
    left: 66px;
    top: 100px;
    margin: 0;
    font-family: "Open Sans", sans-serif;
    font-weight: 800;
    font-size: 36px;
    color: var(--brand-blue);
    letter-spacing: -0.3px;
  }
  .person {
    position: absolute;
    left: 94px;
    top: 326px;
  }
  .person__name {
    margin: 0;
    font-family: "Open Sans", sans-serif;
    font-weight: 800;
    font-size: 24px;
    line-height: 28px;
    color: var(--brand-deep);
  }
  .person__role {
    margin: 0;
    font-family: "Roboto", sans-serif;
    font-weight: 400;
    font-size: 17px;
    line-height: 20px;
    color: #3d8bc9;
  }
  .contact {
    position: absolute;
    right: 66px;
    top: 252px;
    text-align: right;
    font-family: "Roboto", sans-serif;
    font-weight: 300;
    font-size: 17px;
    line-height: 21.5px;
    color: var(--paper);
  }
  .contact__address { margin: 0 0 11px; }
  .contact__list { list-style: none; margin: 0; padding: 0; }
  .contact__item {
    display: flex;
    justify-content: flex-end;
    align-items: center;
    gap: 8px;
  }
  .contact__icon { width: 14px; height: 14px; flex: none; }
  .back-brand {
    position: absolute;
    left: 0; right: 0;
    top: 178px;
    margin: 0;
    text-align: center;
    font-family: "Open Sans", sans-serif;
    font-weight: 800;
    font-size: 60px;
    line-height: 80px;
    letter-spacing: -0.5px;
    color: var(--paper);
  }
  .services {
    position: absolute;
    left: 0; right: 0;
    top: 290px;
    margin: 0;
    text-align: center;
    font-family: "Open Sans", sans-serif;
    font-weight: 700;
    font-size: 16px;
    color: var(--paper);
  }
  .services__dot { margin: 0 4px; }
</style>
</head>
<body>

<div class="card-slot card-slot--front">
  <section class="card card--front" aria-label="Business card front">
    <svg class="card__shapes" viewBox="0 0 800 457" aria-hidden="true">
      <defs>
        <linearGradient id="sky-ring" x1="0" y1="1" x2="1" y2="0">
          <stop offset="0" stop-color="#2f8fca"/>
          <stop offset="1" stop-color="#6cc4e6"/>
        </linearGradient>
        <linearGradient id="deep-disc" x1="0" y1="1" x2="1" y2="0">
          <stop offset="0" stop-color="#2c66ac"/>
          <stop offset="1" stop-color="#5a93c9"/>
        </linearGradient>
      </defs>
      <circle cx="702" cy="350" r="264" fill="url(#sky-ring)"/>
      <circle cx="686" cy="360" r="241" fill="url(#deep-disc)" stroke="var(--paper)" stroke-width="3"/>
    </svg>

    <h1 class="brand-name">Brightwall Systems</h1>

    <div class="person">
      <p class="person__name">Daniel Carter</p>
      <p class="person__role">President</p>
    </div>

    <address class="contact" style="font-style:normal">
      <p class="contact__address">Brightwall Systems Ltd<br>4210 Lakeview Ave # 118<br>Westfield Ohio 44020</p>
      <ul class="contact__list">
        <li class="contact__item">555.201.3748 ext 104
          <svg class="contact__icon" viewBox="0 0 16 16" aria-hidden="true"><path fill="#fff" d="M3.6 1.2l2.3 2.6-1.3 1.8c.9 2 2.6 3.7 4.6 4.6l1.8-1.3 2.6 2.3-1.2 2.3C8 13.5 2.5 8 1.3 3.2z"/></svg>
        </li>
        <li class="contact__item">info@brightwallinfo.com
          <svg class="contact__icon" viewBox="0 0 16 16" aria-hidden="true"><rect x="1.5" y="4" width="13" height="8.5" fill="#fff"/><path d="M1.5 4l6.5 5 6.5-5" fill="none" stroke="#3276b5" stroke-width="1.2"/></svg>
        </li>
        <li class="contact__item">brightwallinfo.com
          <svg class="contact__icon" viewBox="0 0 16 16" aria-hidden="true"><circle cx="8" cy="8" r="7" fill="#fff"/><path d="M5 4.5c1.5.5 2 2 1 3s.5 2.5 0 4M10 3.5c-.5 1.5.5 2.5 2 2.5M11 9.5c-1 .5-1.2 2-.5 3" fill="none" stroke="#3276b5" stroke-width="1.3"/></svg>
        </li>
      </ul>
    </address>
  </section>
</div>

<div class="card-slot card-slot--back">
  <section class="card card--back" aria-label="Business card back">
    <h2 class="back-brand">Brightwall Systems</h2>
    <p class="services">Video Surveillance<span class="services__dot">•</span>Security Alarm<span class="services__dot">•</span>Fire Alarm<span class="services__dot">•</span>Access Control</p>
  </section>
</div>

</body>
</html>
```